THE GRAND MIDNIGHT RHYTHM REVUE---a CONCERT

We need a web page to support our upcoming concert asap. It is a southern blues concert featuring Dorinda Plackett, Fenwicke, Marcus Quibbley, and Alvin Prosko. We have as special guest local talent from the Augusta, Ga Area---Wroxbury, Ray Dunmo and Ja'Vonne. Hosted By: Augusta's Own--Brassy Kettle.
The concert is as follow:
The Grand Midnight Rhythm Revue
Saturday, July 7, 2018
7:00 pm Doors open at 6:00pm
Corran Hall, Augusta, GA
Tickets are $39, $49 and $59
Tickets on sale at the Box Office(need link to "BUY TICKETS"), Kestrel Records, Marigold Ticket Desk and Camp Ridley, GA
We are honoring all military and first responders and offering discount tickets--contact 770-555-0182 for discount code
Overnight concert guests are invited to stay at the Restwell Lodge in Augusta for a reduced rate of $69--we would like a link to that site. Mention Code:
The Concert is promoted by COPPERVALE DUNMORE PRODUCTIONS
The Corran Hall Logo and Adress must appear somewhere at the bottom or near where the Corran Hall is mentioned.
The Military requires that we say, No government or military endorsement implied.
Picture of the Artists and our current flyer is attached. If you need the layered file--contact us

Target Market(s)

blues music lovers and concert goers

Coding

Coded - Design and coding required

Number of Pages Required

1 page

Colors

Designer to choose colors to be used in the design.

Requirements
Must have
• link to buy tickets/mention chatterbook and peeper
Nice to have
• links to artist sites and hotel, TICKET GIVEAWAY REGISTRATION

```html
<!DOCTYPE html>
<html lang="en">
<head>
<meta charset="utf-8">
<title>The Grand Midnight Rhythm Revue</title>
<link href="https://fonts.googleapis.com/css2?family=Poppins:wght@400;500;600;700&family=Roboto:wght@400;500&family=Oswald:wght@500&display=swap" rel="stylesheet">
<style>
:root{
  --ink:#07070a;
  --night:#0c0b10;
  --purple:#6136cc;
  --gold:#f0a81c;
  --gold-soft:#f5c84a;
  --cream:#f6e7a8;
  --white:#ffffff;
  --line:#5a5a63;
}
*{box-sizing:border-box;margin:0;padding:0}
html,body{width:1200px;height:3377px;overflow:hidden}
body{position:relative;background:var(--ink);color:var(--white);font-family:"Poppins",sans-serif}
.abs{position:absolute}
a{color:inherit;text-decoration:none}

/* hero */
.hero-photo{left:0;top:0;width:1200px;height:650px;
  background:radial-gradient(ellipse at 78% 10%,rgba(240,150,40,.55),transparent 45%),
  radial-gradient(ellipse at 20% 20%,rgba(140,70,220,.7),transparent 55%),
  linear-gradient(180deg,#3b1f78 0%,#241045 45%,#0b0812 100%)}
.nav-rule{left:390px;top:42px;width:420px;height:1px;background:rgba(255,255,255,.45)}
.nav{left:0;top:42px;width:1200px;text-align:center}
.nav ul{list-style:none;display:flex;justify-content:center;gap:34px;font-size:13px;font-weight:600;letter-spacing:.3px;padding-top:20px}
.event-title{left:0;top:180px;width:1200px;text-align:center;font-size:46px;font-weight:600;line-height:64px;color:var(--cream)}
.event-box{left:398px;top:345px;width:403px;height:185px;border:3px solid var(--white);text-align:center;font-size:23px;font-weight:600;line-height:42px;padding-top:22px}
.dots{left:573px;top:587px;display:flex;gap:6px}
.dots span{width:13px;height:13px;border-radius:50%;border:2px solid var(--white)}
.dots span.on{background:var(--white)}

/* tickets */
.ticket{top:646px;width:304px;height:272px;text-align:center;padding-top:34px;
  --n:24px;
  background:
   radial-gradient(circle at 0 0,transparent var(--n),var(--purple) calc(var(--n) + 1px)) top left/51% 51% no-repeat,
   radial-gradient(circle at 100% 0,transparent var(--n),var(--purple) calc(var(--n) + 1px)) top right/51% 51% no-repeat,
   radial-gradient(circle at 0 100%,transparent var(--n),var(--purple) calc(var(--n) + 1px)) bottom left/51% 51% no-repeat,
   radial-gradient(circle at 100% 100%,transparent var(--n),var(--purple) calc(var(--n) + 1px)) bottom right/51% 51% no-repeat}
.ticket-price{font-size:30px;font-weight:600}
.ticket-rule{width:54px;height:3px;background:var(--white);margin:12px auto 22px}
.ticket-copy{font-family:"Roboto",sans-serif;font-size:12.5px;line-height:21px;padding:0 16px}
.ticket-btn{display:inline-block;margin-top:20px;background:var(--gold);color:#2a1800;font-size:13px;font-weight:600;padding:8px 26px;border-radius:20px}

/* honour */
.honour{left:0;top:1012px;width:1200px;text-align:center;font-size:25px;font-weight:500;line-height:44px;color:var(--cream)}
.honour .gold{color:var(--gold)}
.honour .white{color:var(--white)}

/* player */
.band-bg{left:0;top:1190px;width:1200px;height:800px;background:linear-gradient(180deg,#0b0a10,#1a1530 40%,#0d0b12)}
.player{left:150px;top:1253px;width:917px;height:113px;border:2px solid var(--line);background:rgba(20,18,26,.8)}
.player-art{left:117px;top:1238px;width:143px;height:143px;border-radius:50%;border:4px solid var(--white);background:radial-gradient(circle,#8a5a2a,#3a2a4a)}
.player-date{left:275px;top:1278px;font-size:13px;color:var(--gold)}
.player-title{left:275px;top:1298px;font-size:18px;color:var(--white)}
.player-time{left:903px;top:1293px;font-size:12px;color:#55555c}
.player-track{left:275px;top:1333px;width:665px;height:3px;background:#3d3d45}
.player-progress{left:275px;top:1332px;width:108px;height:5px;background:var(--gold)}
.player-ctrl{left:970px;top:1295px}

/* artists */
.section-title{left:0;top:1480px;width:1200px;text-align:center;font-size:33px;font-weight:600}
.artist{top:1586px;width:207px;height:207px;border-radius:50%;border:4px solid var(--white)}
.artist-name{top:1810px;width:240px;text-align:center;font-size:20px;font-weight:500}

/* hotel */
.hotel{left:133px;top:1980px;width:934px;height:180px;border:2px solid #cfcfd6;text-align:center;padding-top:40px;font-size:24px;font-weight:500;line-height:46px}
.hotel .gold{color:var(--gold)}
.hotel-mark{left:500px;top:1958px;width:198px;height:50px;background:#b8161c;border:2px solid var(--white);display:flex;align-items:center;justify-content:center;gap:10px;font-size:17px;font-weight:500;color:var(--white)}
.hotel-mark i{width:14px;height:14px;background:var(--white)}
.promo{left:0;top:2222px;width:1200px;text-align:center;font-size:19px;font-weight:500}
.promo .gold{color:var(--gold)}

/* giveaway */
.give-bg{left:0;top:2367px;width:1200px;height:495px;background:radial-gradient(ellipse at 80% 30%,rgba(200,120,40,.45),transparent 50%),linear-gradient(180deg,#2a2218,#14110e 60%,#0a0908)}
.give-icon{left:565px;top:2484px;width:70px;height:70px;border-radius:50%;border:3px solid var(--white)}
.give-title{left:0;top:2562px;width:1200px;text-align:center;font-size:40px;font-weight:600;letter-spacing:1px}
.give-sub{left:0;top:2626px;width:1200px;text-align:center;font-family:"Roboto",sans-serif;font-size:17px}
.field{top:2688px;width:278px;height:40px;border-radius:20px;background:var(--white);color:#999;font-family:"Roboto",sans-serif;font-size:12px;padding:12px 20px}
.give-btn{left:818px;top:2688px;width:155px;height:40px;border-radius:20px;background:var(--gold);color:#2a1800;font-size:14px;font-weight:600;text-align:center;line-height:40px}

/* notice */
.notice-bg{left:0;top:2862px;width:1200px;height:228px;background:linear-gradient(135deg,#4b4a32,#2e2e22 40%,#545338 70%,#2c2b20)}
.notice{left:0;top:2935px;width:1200px;text-align:center;font-family:"Oswald",sans-serif;font-size:30px;font-weight:500;line-height:45px;text-transform:uppercase}

/* footer */
.footer-bg{left:0;top:3090px;width:1200px;height:287px;background:var(--night)}
.footer-brand{left:100px;top:3200px;width:200px;text-align:center;font-size:22px;font-weight:600;line-height:30px;color:var(--gold-soft)}
.social{left:0;top:3170px;width:1200px;display:flex;justify-content:center;gap:28px}
.social a{display:flex;align-items:center;gap:8px;font-size:14px;font-weight:500}
.social i{width:30px;height:30px;border-radius:50%;background:var(--white)}
.footer-nav{left:0;top:3240px;width:1200px;text-align:center;font-size:12px}
.copy{left:0;top:3280px;width:1200px;text-align:center;font-size:12px}
.venue{left:915px;top:3168px;display:flex;align-items:center;gap:10px;font-size:20px;font-weight:600}
.venue i{width:56px;height:56px;border-radius:50%;background:#3f6f98;border:3px solid var(--white)}
</style>
</head>
<body>

<header>
  <div class="abs hero-photo" role="img" aria-label="Concert crowd with raised hands under purple and amber stage lights"></div>
  <div class="abs nav-rule"></div>
  <nav class="abs nav"><ul><li>HOME</li><li>ABOUT</li><li>MY MUSIC</li><li>BLOG</li><li>CONTACT US</li></ul></nav>
  <h1 class="abs event-title">The Grand Midnight<br>Rhythm Revue</h1>
  <div class="abs event-box">Saturday, July 7, 2018<br>7:00 pm Doors open at 6:00pm<br>Corran Hall, Augusta, GA</div>
  <div class="abs dots"><span class="on"></span><span></span><span></span></div>
</header>

<section class="tickets">
  <div class="abs ticket" style="left:130px"><div class="ticket-price">$39</div><div class="ticket-rule"></div><p class="ticket-copy">Sed ut perspiciatis unde omnis iste natus error sit voluptatem accusantium doloremque laudantium, totam rem aperiam</p><a class="ticket-btn" href="#">BUY TICKETS</a></div>
  <div class="abs ticket" style="left:449px"><div class="ticket-price">$49</div><div class="ticket-rule"></div><p class="ticket-copy">Sed ut perspiciatis unde omnis iste natus error sit voluptatem accusantium doloremque laudantium, totam rem aperiam</p><a class="ticket-btn" href="#">BUY TICKETS</a></div>
  <div class="abs ticket" style="left:767px"><div class="ticket-price">$59</div><div class="ticket-rule"></div><p class="ticket-copy">Sed ut perspiciatis unde omnis iste natus error sit voluptatem accusantium doloremque laudantium, totam rem aperiam</p><a class="ticket-btn" href="#">BUY TICKETS</a></div>
</section>

<p class="abs honour">We Are Honoring All Military And First Responders<br>And Offering Discount <span class="gold">Tickets</span><br><span class="white">Contact</span> <span class="gold">770-555-0182</span> <span class="white">For Discount</span> <span class="gold">Code</span></p>

<div class="abs band-bg" role="img" aria-label="Dim photo of a blues band on stage"></div>
<section class="audio">
  <div class="abs player"></div>
  <div class="abs player-art" role="img" aria-label="Album cover artwork of the performers"></div>
  <div class="abs player-date">Friday, 15 June 2018</div>
  <div class="abs player-title">THE MIDNIGHT RHYTHM JAM</div>
  <div class="abs player-time">00:00</div>
  <div class="abs player-track"></div>
  <div class="abs player-progress"></div>
  <svg class="abs player-ctrl" width="80" height="30" viewBox="0 0 80 30" aria-label="Playback controls">
    <circle cx="12" cy="15" r="10" fill="#2a2a30"/><path d="M16 10v10l-5-5zM11 10v10l-5-5z" fill="#fff"/>
    <circle cx="40" cy="15" r="13" fill="#fff"/><path d="M36 9v12l10-6z" fill="#111"/>
    <circle cx="68" cy="15" r="10" fill="#2a2a30"/><path d="M64 10v10l5-5zM69 10v10l5-5z" fill="#fff"/>
  </svg>
</section>

<section class="artists">
  <h2 class="abs section-title">SOUTHERN BLUES CONCERT</h2>
  <div class="abs artist" style="left:133px;background:radial-gradient(circle,#4c6f86,#1d3344)" role="img" aria-label="Portrait of Dorinda Plackett"></div>
  <div class="abs artist" style="left:374px;background:radial-gradient(circle,#c0602a,#5a2410)" role="img" aria-label="Portrait of Fenwicke"></div>
  <div class="abs artist" style="left:615px;background:radial-gradient(circle,#d89a2a,#5a2a08)" role="img" aria-label="Portrait of Marcus Quibbley"></div>
  <div class="abs artist" style="left:856px;background:radial-gradient(circle,#8a5ad8,#3a1a78)" role="img" aria-label="Portrait of Alvin Prosko"></div>
  <div class="abs artist-name" style="left:116px">Dorinda Plackett</div>
  <div class="abs artist-name" style="left:357px">Fenwicke</div>
  <div class="abs artist-name" style="left:598px">Marcus Quibbley</div>
  <div class="abs artist-name" style="left:839px">Alvin Prosko</div>
</section>

<section class="stay">
  <p class="abs hotel">Overnight <span class="gold">concert guests</span> are invited to stay<br>at the <a class="gold" href="#">Restwell Lodge</a> in Augusta for a reduced rate of <span class="gold">$69</span></p>
  <div class="abs hotel-mark"><i></i>Restwell Lodge</div>
  <p class="abs promo">The Concert is <span class="gold">Promoted by</span> COPPERVALE DUNMORE PRODUCTIONS</p>
</section>

<section class="giveaway">
  <div class="abs give-bg" role="img" aria-label="DJ mixing desk under warm stage lights"></div>
  <svg class="abs give-icon" viewBox="0 0 70 70" aria-label="Ticket icon"><rect x="20" y="24" width="30" height="22" rx="3" fill="none" stroke="#fff" stroke-width="3"/><line x1="26" y1="32" x2="44" y2="32" stroke="#fff" stroke-width="3"/><line x1="26" y1="38" x2="44" y2="38" stroke="#fff" stroke-width="3"/></svg>
  <h2 class="abs give-title">TICKET GIVE AWAY</h2>
  <p class="abs give-sub">Midnight Rhythm Revue Concert</p>
  <div class="abs field" style="left:226px">Phone</div>
  <div class="abs field" style="left:522px">Email address</div>
  <a class="abs give-btn" href="#">GET STARTED</a>
</section>

<div class="abs notice-bg" role="img" aria-label="Camouflage texture band"></div>
<p class="abs notice">The military requires that we say,<br>No government or military endorsement implied.</p>

<footer>
  <div class="abs footer-bg"></div>
  <div class="abs footer-brand">The Grand Midnight Rhythm Revue</div>
  <div class="abs social"><a href="#"><i></i>peeper</a><a href="#"><i></i>chatterbook</a></div>
  <p class="abs footer-nav">Home &nbsp;/&nbsp; About &nbsp;/&nbsp; My Music &nbsp;/&nbsp; Blog &nbsp;/&nbsp; Contact</p>
  <p class="abs copy">2018 © Copyrights The Grand Midnight Rhythm Revue.All Rights Reserved</p>
  <div class="abs venue"><i></i>Corran Hall</div>
</footer>

</body>
</html>
```